I need the Scorecard I've developed for my staff to be produced into a visually engaging piece that will encourage the staff to utilize it on a daily basis. I'm thinking it could be 5x7 in size so that it isn't too cumbersome, but I'm open to different layouts.
I have multiple other departments that will need Scorecards created for them as well, but each one will contain task specific questions for each department.

```html
<!DOCTYPE html>
<html lang="en">
<head>
<meta charset="utf-8">
<title>Receptionist Daily Excellence Scorecard</title>
<link rel="stylesheet" href="https://fonts.googleapis.com/css2?family=Lexend:wght@400;500;600;700&family=Fira+Sans:wght@500;600;700&family=Open+Sans:wght@400;600;700&display=swap">
<style>
:root{
  --navy:#0b3a66;
  --blue:#0a67c2;
  --blue-deep:#0656a8;
  --teal:#0bb6c9;
  --teal-bright:#11c4c9;
  --card-line:#27c6d2;
  --ink:#1c2533;
  --muted:#4a5563;
  --rule:#c9ced6;
  --soft:#f2f3f5;
  --white:#ffffff;
}
*{box-sizing:border-box;margin:0;padding:0}
html,body{width:1200px;height:3143px;overflow:hidden}
body{position:relative;background:linear-gradient(to bottom,var(--white) 0,var(--white) 2400px,var(--soft) 2400px);font-family:"Open Sans",Arial,sans-serif;color:var(--ink)}

.sheet{position:absolute;left:83px;width:1036px;height:1450px;background:var(--white);box-shadow:0 8px 26px rgba(20,40,70,.22)}
.sheet-tasks{top:84px}
.sheet-summary{top:1610px;height:1451px;background:linear-gradient(160deg,#08b8b2 0%,#0a8ec0 40%,#0a6fc2 100%)}

/* header */
.header{position:absolute;left:0;top:0;width:100%;height:202px;background:linear-gradient(100deg,#0a5fb3 0%,#0a7cbd 55%,#0aa2bb 100%)}
.stars{position:absolute;top:22px;left:0;width:100%;display:flex;justify-content:center;gap:8px}
.title{position:absolute;top:60px;width:100%;text-align:center;font-family:"Lexend",sans-serif;font-weight:600;font-size:36px;color:var(--white)}
.id-bar{position:absolute;left:102px;top:126px;width:831px;height:52px;background:var(--white);border-radius:14px;display:flex;align-items:center;padding:0 26px;gap:38px;font-family:"Lexend",sans-serif;font-size:16px;color:var(--ink)}
.id-field{display:flex;align-items:flex-end;flex:1}
.id-field span.line{flex:1;border-bottom:1px solid var(--rule);margin-left:6px;height:14px}
.instructions{position:absolute;top:216px;width:100%;text-align:center;font-family:"Lexend",sans-serif;font-style:italic;font-size:16.5px;font-weight:300;color:var(--ink)}

/* cards */
.card{position:absolute;width:289px;height:535px;border:2px solid var(--card-line);border-radius:24px;background:var(--white)}
.card-clip{position:absolute;inset:0;border-radius:22px;overflow:hidden}
.rating-strip{position:absolute;right:0;bottom:0;width:93px;border-top-left-radius:10px}
.rating-strip .label{display:block;padding:6px 0 0 10px;font-family:"Lexend",sans-serif;font-weight:600;font-size:13px;line-height:1.05;color:var(--white)}
.rating-strip .label small{display:block;font-size:11px;font-weight:500}
.strip-teal{background:var(--teal)}
.strip-blue{background:var(--blue)}
.emblem{position:absolute;left:50%;top:-30px;width:52px;height:52px;margin-left:-26px;transform:rotate(45deg);background:var(--white);border:2px solid var(--card-line);border-radius:10px;z-index:2}
.emblem svg{position:absolute;left:50%;top:50%;transform:translate(-50%,-50%) rotate(-45deg)}
.card-title{position:absolute;left:25px;top:21px;width:235px;height:59px;border-radius:16px;display:flex;align-items:center;justify-content:center;text-align:center;font-family:"Lexend",sans-serif;font-weight:500;font-size:19px;line-height:1.2;color:var(--white);z-index:1}
.title-blue{background:var(--blue-deep)}
.title-teal{background:var(--teal)}
.task-label{position:absolute;left:24px;font-family:"Lexend",sans-serif;font-weight:500;font-size:13px;color:var(--blue-deep)}
.task{position:absolute;left:12px;width:267px;background:var(--white);border-radius:9px;box-shadow:0 1px 4px rgba(0,0,0,.16);padding:10px 12px}
.task::after{content:"";position:absolute;left:181px;top:12px;width:1px;height:30px;background:#aab2bd}
.task-name{width:170px;font-family:"Lexend",sans-serif;font-weight:600;font-size:13px;line-height:1.3;color:var(--ink)}
.task-notes{position:absolute;left:12px;bottom:10px;font-family:"Lexend",sans-serif;font-size:13px;color:var(--muted)}

/* summary page */
.panel{position:absolute;left:57px;top:55px;width:921px;height:1396px;background:var(--white);border-radius:52px 52px 0 0;overflow:hidden}
.summary-heading{position:absolute;top:36px;width:100%;text-align:center;font-family:"Fira Sans",sans-serif;font-weight:700;font-size:32px;color:var(--navy)}
.summary-heading em{font-style:normal;color:var(--teal)}
.summary-rule{position:absolute;left:185px;top:84px;width:550px;height:3px;background:#d3d7dd}
.status-list{position:absolute;left:68px;top:100px;list-style:none;font-size:24px;line-height:36px;color:var(--ink)}
.status-list li{display:flex;align-items:center;gap:16px}
.dot{width:22px;height:22px;border-radius:50%}
.dot-teal{background:var(--teal)}
.dot-navy{background:var(--navy)}
.reflection{position:absolute;left:0;top:284px;width:100%;height:395px;background:var(--soft)}
.reflection-pill{position:absolute;left:311px;top:257px;width:298px;height:54px;border-radius:27px;background:linear-gradient(90deg,var(--blue-deep),var(--teal-bright));display:flex;align-items:center;justify-content:center;gap:10px;font-family:"Fira Sans",sans-serif;font-weight:700;font-size:30px;color:var(--white);z-index:2}
.question{position:absolute;left:87px;font-size:24px;color:var(--ink)}
.answer{position:absolute;left:87px;width:747px;height:52px;border-radius:26px;background:var(--white)}
.divider{position:absolute;left:68px;top:719px;width:783px;height:2px;background:#c5cad2}
.sf-heading{position:absolute;top:763px;width:100%;display:flex;justify-content:center;align-items:center;gap:6px;font-family:"Fira Sans",sans-serif;font-weight:600;font-size:24px;color:var(--navy)}
.sf-heading em{font-style:normal;color:var(--teal)}
.sf-box{position:absolute;left:68px;width:783px;height:121px;border:2px solid #cfd4da;border-radius:16px;padding:14px 20px;font-family:"Fira Sans",sans-serif;font-weight:600;font-size:22px;color:var(--ink);display:flex;align-items:flex-start;gap:8px}
.manager-label{position:absolute;left:92px;top:1106px;font-family:"Fira Sans",sans-serif;font-weight:700;font-size:27px;color:var(--navy)}
.manager-note{position:absolute;left:92px;top:1150px;font-size:13px;color:var(--navy)}
.manager-box{position:absolute;left:490px;top:1102px;width:334px;height:68px;border:2px solid #cfd4da;border-radius:14px}
.sign-row{position:absolute;left:89px;top:1248px;width:740px;display:flex;gap:38px;font-size:16px;color:var(--ink)}
.sign{display:flex;align-items:flex-end;flex:1}
.sign .line{flex:1;border-bottom:1px solid var(--rule);margin-left:6px;height:16px}
.date-row{position:absolute;left:346px;top:1297px;width:230px;display:flex;font-size:16px}
.date-row .line{flex:1;border-bottom:1px solid var(--rule);margin-left:6px;height:16px}
</style>
</head>
<body>

<section class="sheet sheet-tasks">
  <header class="header">
    <div class="stars">
      <svg width="28" height="28" viewBox="0 0 24 24"><path d="M12 1.8l3 6.6 7.1.7-5.4 4.8 1.6 7-6.3-3.7-6.3 3.7 1.6-7L1.9 9.1 9 8.4z" fill="#ffd21a"/></svg>
      <svg width="28" height="28" viewBox="0 0 24 24"><path d="M12 1.8l3 6.6 7.1.7-5.4 4.8 1.6 7-6.3-3.7-6.3 3.7 1.6-7L1.9 9.1 9 8.4z" fill="#ffd21a"/></svg>
      <svg width="28" height="28" viewBox="0 0 24 24"><path d="M12 1.8l3 6.6 7.1.7-5.4 4.8 1.6 7-6.3-3.7-6.3 3.7 1.6-7L1.9 9.1 9 8.4z" fill="#ffd21a"/></svg>
      <svg width="28" height="28" viewBox="0 0 24 24"><path d="M12 1.8l3 6.6 7.1.7-5.4 4.8 1.6 7-6.3-3.7-6.3 3.7 1.6-7L1.9 9.1 9 8.4z" fill="#ffd21a"/></svg>
      <svg width="28" height="28" viewBox="0 0 24 24"><path d="M12 1.8l3 6.6 7.1.7-5.4 4.8 1.6 7-6.3-3.7-6.3 3.7 1.6-7L1.9 9.1 9 8.4z" fill="#ffd21a"/></svg>
    </div>
    <h1 class="title">Receptionist Daily Excellence Scorecard</h1>
    <div class="id-bar">
      <div class="id-field">Name:<span class="line"></span></div>
      <div class="id-field">Date:<span class="line"></span></div>
      <div class="id-field">Location:<span class="line"></span></div>
    </div>
  </header>
  <p class="instructions">(Please rate yourself for each task: 1 = Needs Improvement, 3 = Meets Expectations, 5 = Excellent)</p>

  <!-- Row 1 -->
  <article class="card" style="left:52px;top:290px">
    <div class="card-clip"><div class="rating-strip strip-teal" style="top:89px"><span class="label">Self-Rating<small>(1-5)</small></span></div></div>
    <div class="emblem"><svg width="26" height="26" viewBox="0 0 24 24" fill="none" stroke="#0a67c2" stroke-width="2"><path d="M5 13v-2a7 7 0 0114 0v2"/><rect x="3" y="12" width="4" height="6" rx="1.5" fill="#0a67c2"/><rect x="17" y="12" width="4" height="6" rx="1.5" fill="#0a67c2"/><circle cx="12" cy="11" r="3" fill="#0a67c2"/></svg></div>
    <h2 class="card-title title-blue">Call Handling &amp;<br>First Call Intake</h2>
    <span class="task-label" style="top:108px">Task:</span>
    <div class="task" style="top:137px;height:87px"><p class="task-name">Answered 90%+ calls within 3 rings</p><p class="task-notes">Notes / Issues:</p></div>
    <div class="task" style="top:237px;height:87px"><p class="task-name">Maintained empathy and professionalism</p><p class="task-notes">Notes / Issues:</p></div>
    <div class="task" style="top:337px;height:87px"><p class="task-name">Accurately completed all First Call fields</p><p class="task-notes">Notes / Issues:</p></div>
    <div class="task" style="top:437px;height:87px"><p class="task-name">Worked within Receptionist role</p><p class="task-notes">Notes / Issues:</p></div>
  </article>

  <article class="card" style="left:373px;top:290px">
    <div class="card-clip"><div class="rating-strip strip-blue" style="top:89px"><span class="label">Self-Rating<small>(1-5)</small></span></div></div>
    <div class="emblem"><svg width="26" height="26" viewBox="0 0 24 24" fill="#0bb6c9"><path d="M6.6 3.5l2.6 3.6-1.7 2.2a11 11 0 005.2 5.2l2.2-1.7 3.6 2.6-1.5 3.3C10 18.5 5.5 14 4.4 5.6z"/></svg></div>
    <h2 class="card-title title-teal">Call Management<br>During Busy Times</h2>
    <span class="task-label" style="top:108px">Task:</span>
    <div class="task" style="top:137px;height:87px"><p class="task-name">Prioritized urgent vs. non-urgent calls</p><p class="task-notes">Notes / Issues:</p></div>
    <div class="task" style="top:237px;height:87px"><p class="task-name">Hold times under minute 1</p><p class="task-notes">Notes / Issues:</p></div>
    <div class="task" style="top:337px;height:87px"><p class="task-name">Logged all calls</p><p class="task-notes">Notes / Issues:</p></div>
    <div class="task" style="top:437px;height:87px"><p class="task-name">Requested help if overwhelmed</p><p class="task-notes">Notes / Issues:</p></div>
  </article>

  <article class="card" style="left:694px;top:290px">
    <div class="card-clip"><div class="rating-strip strip-teal" style="top:89px"><span class="label">Self-Rating<small>(1-5)</small></span></div></div>
    <div class="emblem"><svg width="26" height="26" viewBox="0 0 24 24" fill="none" stroke="#0a67c2" stroke-width="2"><rect x="3" y="5" width="15" height="14" rx="2"/><path d="M3 9h15M7 3v4M14 3v4"/><circle cx="18" cy="17" r="4" fill="#fff"/><path d="M18 15v2l1.2 1"/></svg></div>
    <h2 class="card-title title-blue">Scheduling Accuracy</h2>
    <span class="task-label" style="top:108px">Task:</span>
    <div class="task" style="top:137px;height:87px"><p class="task-name">Updated scheduling board</p><p class="task-notes">Notes / Issues:</p></div>
    <div class="task" style="top:237px;height:87px"><p class="task-name">Cross-checked with Red Book</p><p class="task-notes">Notes / Issues:</p></div>
    <div class="task" style="top:337px;height:87px"><p class="task-name">Entered manifold info promptly</p><p class="task-notes">Notes / Issues:</p></div>
  </article>

  <!-- Row 2 -->
  <article class="card" style="left:52px;top:875px">
    <div class="card-clip"><div class="rating-strip strip-blue" style="top:88px"><span class="label">Self-Rating<small>(1-5)</small></span></div></div>
    <div class="emblem"><svg width="26" height="26" viewBox="0 0 24 24" fill="none" stroke="#0bb6c9" stroke-width="1.8"><path d="M12 4c2 2.5 2 6 0 9-2-3-2-6.5 0-9z"/><path d="M12 13c-3-.5-5-3-5.5-6 3 .5 5 3 5.5 6zM12 13c3-.5 5-3 5.5-6-3 .5-5 3-5.5 6z"/><path d="M4 16c4 1 12 1 16 0"/></svg></div>
    <h2 class="card-title title-teal">Clothing &amp; Flowers</h2>
    <span class="task-label" style="top:102px">Task:</span>
    <div class="task" style="top:126px;height:76px"><p class="task-name">Clothing sheet completed</p><p class="task-notes">Notes / Issues:</p></div>
    <div class="task" style="top:208px;height:76px"><p class="task-name">Family contact noted on sheet</p><p class="task-notes">Notes / Issues:</p></div>
    <div class="task" style="top:290px;height:76px"><p class="task-name">Floral deliveries logged</p><p class="task-notes">Notes / Issues:</p></div>
    <div class="task" style="top:372px;height:76px"><p class="task-name" style="width:176px">Concerns communicated to Care Center</p><p class="task-notes">Notes / Issues:</p></div>
    <div class="task" style="top:454px;height:76px"><p class="task-name">Flower placement verified</p><p class="task-notes">Notes / Issues:</p></div>
  </article>

  <article class="card" style="left:373px;top:875px">
    <div class="card-clip"><div class="rating-strip strip-teal" style="top:96px"><span class="label">Self-Rating<small>(1-5)</small></span></div></div>
    <div class="emblem"><svg width="26" height="26" viewBox="0 0 24 24" fill="#0a67c2"><path d="M6 3h9l4 4v14H6z"/><path d="M15 3v4h4" fill="#5aa0e0"/><rect x="9" y="10" width="7" height="1.6" fill="#fff"/><rect x="9" y="13.5" width="7" height="1.6" fill="#fff"/><rect x="9" y="17" width="4" height="1.6" fill="#fff"/></svg></div>
    <h2 class="card-title title-blue">Death Certificates</h2>
    <span class="task-label" style="top:110px">Task:</span>
    <div class="task" style="top:135px;height:87px"><p class="task-name">Verified recipient ID &amp; relationship</p><p class="task-notes">Notes / Issues:</p></div>
    <div class="task" style="top:235px;height:87px"><p class="task-name">Confirmed correct documents enclosed</p><p class="task-notes">Notes / Issues:</p></div>
    <div class="task" style="top:335px;height:87px"><p class="task-name">Recipient signed the DC logbook</p><p class="task-notes">Notes / Issues:</p></div>
    <div class="task" style="top:435px;height:87px"><p class="task-name">Suggested proofreading before leaving</p><p class="task-notes">Notes / Issues:</p></div>
  </article>

  <article class="card" style="left:694px;top:875px">
    <div class="card-clip"><div class="rating-strip strip-blue" style="top:96px"><span class="label">Self-Rating<small>(1-5)</small></span></div></div>
    <div class="emblem"><svg width="26" height="26" viewBox="0 0 24 24" fill="#0a67c2"><path d="M3 4h13v9H8l-4 3v-3H3z"/><path d="M18 8h3v9h-1v3l-4-3h-6v-2h8z" fill="#0bb6c9"/></svg></div>
    <h2 class="card-title title-teal">Routing &amp; Messages</h2>
    <span class="task-label" style="top:110px">Task:</span>
    <div class="task" style="top:135px;height:87px"><p class="task-name">Calls routed appropriately</p><p class="task-notes">Notes / Issues:</p></div>
    <div class="task" style="top:235px;height:87px"><p class="task-name">Messages included all required info</p><p class="task-notes">Notes / Issues:</p></div>
    <div class="task" style="top:335px;height:87px"><p class="task-name">+Delivered 95% messages in 30 min</p><p class="task-notes">Notes / Issues:</p></div>
  </article>
</section>

<section class="sheet sheet-summary">
  <div class="panel">
    <h2 class="summary-heading">Daily Status Summary <em>(Circle One)</em></h2>
    <div class="summary-rule"></div>
    <ul class="status-list">
      <li><span class="dot dot-teal"></span>Excellent – All key duties completed, proactive, calm under pressure</li>
      <li><span class="dot dot-navy"></span>Satisfactory – Most duties completed, minor follow-up needed</li>
      <li><span class="dot dot-teal"></span>Needs Support – Missed urgent duties, accuracy or stress issues</li>
    </ul>

    <div class="reflection"></div>
    <div class="reflection-pill">
      <svg width="28" height="28" viewBox="0 0 24 24" fill="none" stroke="#fff" stroke-width="2"><path d="M20 12a8 8 0 11-2.4-5.7"/><path d="M18 2v5h-5"/><path d="M12 8v4l3 2"/></svg>
      Daily Reflection
    </div>
    <p class="question" style="top:336px">What went well today?</p>
    <div class="answer" style="top:375px"></div>
    <p class="question" style="top:446px">Any issues or barriers to note?</p>
    <div class="answer" style="top:485px"></div>
    <p class="question" style="top:556px">Support needed from supervisor?</p>
    <div class="answer" style="top:595px"></div>

    <div class="divider"></div>
    <h3 class="sf-heading">
      <svg width="24" height="24" viewBox="0 0 24 24" fill="#f5c518"><path d="M12 2l2 7 7 2-7 2-2 7-2-7-7-2 7-2z"/></svg>Stars &amp;
      <svg width="24" height="24" viewBox="0 0 24 24"><path d="M5 2v20" stroke="#555" stroke-width="2"/><path d="M6 3h13l-3 5 3 5H6z" fill="#e02424"/></svg>
      Flags (<em>Supervisor Use Only</em>)
    </h3>
    <div class="sf-box" style="top:824px"><svg width="24" height="24" viewBox="0 0 24 24" fill="#f5c518"><path d="M12 2l2 7 7 2-7 2-2 7-2-7-7-2 7-2z"/></svg>Stars (Excellence or above-and-beyond moments):</div>
    <div class="sf-box" style="top:961px"><svg width="24" height="24" viewBox="0 0 24 24"><path d="M5 2v20" stroke="#555" stroke-width="2"/><path d="M6 3h13l-3 5 3 5H6z" fill="#e02424"/></svg>Flags (Concerns needing follow-up/coaching):</div>

    <p class="manager-label">Manager Overall Rating (1-5):</p>
    <p class="manager-note">(Manager: Please rate overall performance on a 1-5 scale)</p>
    <div class="manager-box"></div>

    <div class="sign-row">
      <div class="sign">Receptionist Signature:<span class="line"></span></div>
      <div class="sign">Supervisor Signature:<span class="line"></span></div>
    </div>
    <div class="date-row">Date:<span class="line"></span></div>
  </div>
</section>

</body>
</html>
```